KRV Inc Web Design

WHAT ARE WE DOING?
We are developing a new website look and feel for a new company called KRV Inc. This new look and feel should include colors, design elements, choice of photography and other imagery, fonts, and other user experience elements.

WHAT DO THEY DO?
KRV, Inc, makes tools for researchers who are studying protein-protein interactions. These molecules are the basic tools of biology, and serve as key targets for drug developers and disease researchers. The world of proteins is enormously complex, and companies like KRV provide researchers with critical tools that help them elucidate this world.

WHO ARE WE TALKING TO?
The target audience for this website are professional scientists working in university research or biopharma drug development. They are highly sophisticated consumers looking for key tools that will advance their research.

WHAT DO WE WANT THEM TO DO?
The site is an information resource for the customer exploring the tools that KRV sells and the scientific issues surrounding protein-protein interactions. They should be able to navigate easily to their content of choice, while the whole site should convey a professionalism that enhanced KRV’s credibility.

WHAT DOES THE KRV BRAND STAND FOR?
KRV stands for illumination. Proteins are challenging to study, and KRV exists to help shed light on their workings.

WHAT ARE THE KEY VALUES OF THE KRV BRAND?
Integrity. Innovation. Insight.

WHAT ARE THE EXECUTIONAL MANDITORIES?
The look and feel is completely up for grabs. Nothing is off the table.

WHAT ARE THE DELIVERABLES?
We need new designs for the following templates:
http://cms.thevormelgroup.com/
http://cms.thevormelgroup.com/products-and-services/instruments-3/bench-top-instruments/
http://cms.thevormelgroup.com/category/lab-study/

```html
<!DOCTYPE html>
<html lang="en">
<head>
<meta charset="utf-8">
<title>KRV Inc — Home</title>
<link rel="stylesheet" href="https://fonts.googleapis.com/css2?family=Questrial&family=Didact+Gothic&family=Montserrat:wght@600;700&display=swap">
<style>
  :root {
    --backdrop: #e6e6e6;
    --white: #ffffff;
    --rule: #8a8a8a;
    --ink: #3c3c3c;
    --ink-soft: #555555;
    --muted: #888888;
    --sky-top: #63bdeb;
    --sky-bottom: #1a88cf;
    --orange-top: #f7962a;
    --orange-bottom: #e2531a;
    --navy-top: #3f6f9c;
    --navy-bottom: #244e79;
    --green: #7bbd32;
    --amber: #e77d23;
    --azure: #168bd6;
    --footer: #3b3533;
    --footer-ink: #e4e1df;
  }
  * { box-sizing: border-box; margin: 0; padding: 0; }
  html, body { width: 1200px; height: 999px; overflow: hidden; background: var(--backdrop); }
  body { position: relative; font-family: "Questrial", sans-serif; color: var(--ink); }

  .page {
    position: absolute; left: 168px; top: 16px;
    width: 720px; height: 806px;
    transform: scale(1.2); transform-origin: 0 0;
    background: var(--white);
  }
  .page > * { position: absolute; }

  .top-rule { left: 0; top: 0; width: 720px; height: 4px; background: var(--rule); }

  .brand { left: 112px; top: 15px; font-family: "Didact Gothic", sans-serif; font-size: 25px; letter-spacing: 2px; color: var(--ink-soft); }

  .search { left: 438px; top: 18px; width: 140px; height: 18px; border: 1px solid #9a9a9a; font-size: 9px; color: #8c8c8c; display: flex; align-items: center; justify-content: center; letter-spacing: .5px; }
  .search-icon { left: 582px; top: 12px; width: 32px; height: 32px; }

  .hero-band { left: 0; top: 51px; width: 720px; height: 284px; background: linear-gradient(var(--sky-top), var(--sky-bottom)); }
  .hero-floor { left: 0; top: 335px; width: 720px; height: 80px; }

  .slider-frame { left: 75px; top: 83px; width: 567px; height: 290px; background: linear-gradient(#d4d4d4, #a9a9a9); }
  .slide { left: 80px; top: 88px; width: 558px; height: 279px; background: linear-gradient(#f6f6f6, #dadada); overflow: hidden; }
  .slide > * { position: absolute; }
  .slide-photo { right: 0; top: 0; width: 228px; height: 279px; background: linear-gradient(160deg, #ededed 0%, #d7d9e0 55%, #8a8fb0 100%); }
  .caption-box { left: 30px; top: 80px; width: 310px; height: 50px; background: #f4f4f4; border: 1px solid #9a9a9a; }
  .caption-box p { position: absolute; left: 36px; top: 8px; font-family: "Montserrat", sans-serif; font-weight: 600; font-size: 12.5px; line-height: 17px; color: #333; white-space: nowrap; }
  .blog-button { left: 102px; top: 188px; width: 156px; height: 30px; border-radius: 4px; background: linear-gradient(var(--orange-top), var(--orange-bottom)); color: #fff; font-family: "Montserrat", sans-serif; font-weight: 600; font-size: 14px; display: flex; align-items: center; justify-content: center; gap: 8px; box-shadow: 0 1px 2px rgba(0,0,0,.3); }

  .slider-dots { left: 324px; top: 382px; display: flex; gap: 3px; }
  .slider-dots span { width: 11px; height: 11px; border-radius: 50%; border: 1px solid #a0a0a0; background: linear-gradient(#fff, #d0d0d0); }
  .slider-dots .is-active { background: #8a8a8a; }

  .main-nav { left: 28px; top: 431px; height: 36px; display: flex; align-items: center; font-size: 15px; color: var(--ink); }
  .main-nav a { color: inherit; text-decoration: none; padding: 0 11px; border-left: 1px solid #555; line-height: 36px; }
  .main-nav a:first-child { border-left: 0; padding-left: 8px; }
  .nav-curve { left: 0; top: 462px; width: 720px; height: 16px; }

  .feature-divider { top: 483px; height: 218px; border-left: 1px dotted #b5b5b5; }
  .feature { top: 497px; width: 200px; text-align: center; }
  .feature-icon { display: block; margin: 0 auto; width: 68px; height: 74px; }
  .feature h2 { font-family: "Montserrat", sans-serif; font-weight: 600; font-size: 14.5px; color: #333; margin-top: 8px; letter-spacing: .3px; }
  .feature-text { height: 86px; margin-top: 10px; text-align: left; font-size: 9.4px; line-height: 11.2px; color: #444; }
  .feature-text span { display: block; margin-bottom: 11px; }
  .feature-button { display: flex; align-items: center; justify-content: center; gap: 9px; width: 134px; height: 26px; margin: 0 auto; border-radius: 4px; background: linear-gradient(var(--navy-top), var(--navy-bottom)); color: #fff; font-family: "Montserrat", sans-serif; font-weight: 600; font-size: 12.5px; }

  .site-footer { left: 0; top: 746px; width: 720px; height: 40px; background: var(--footer); display: flex; align-items: center; justify-content: flex-end; padding-right: 69px; font-size: 14.5px; color: var(--footer-ink); letter-spacing: .3px; }
  .site-footer .sep { margin: 0 6px; }
  .copyright { left: 0; top: 790px; width: 720px; text-align: center; font-size: 9.5px; color: var(--muted); }
</style>
</head>
<body>
<main class="page">
  <div class="top-rule"></div>
  <div class="brand">KRV INC</div>
  <div class="search">Search the Site</div>
  <svg class="search-icon" viewBox="0 0 32 32" aria-hidden="true">
    <circle cx="13" cy="13" r="9" fill="#fff" stroke="#f08a1c" stroke-width="3"/>
    <line x1="19.5" y1="19.5" x2="29" y2="29" stroke="#333" stroke-width="4" stroke-linecap="round"/>
  </svg>

  <div class="hero-band"></div>
  <svg class="hero-floor" viewBox="0 0 720 80" preserveAspectRatio="none" aria-hidden="true">
    <defs><linearGradient id="floor" x1="0" y1="0" x2="0" y2="1"><stop offset="0" stop-color="#d2d2d2"/><stop offset="1" stop-color="#ffffff"/></linearGradient></defs>
    <path d="M0 0H720V30Q360 105 0 30Z" fill="url(#floor)"/>
  </svg>

  <div class="slider-frame"></div>
  <section class="slide">
    <div class="slide-photo" role="img" aria-label="Photograph of a laboratory microscope on a light studio background"></div>
    <div class="caption-box"><p>See what researchers attending<br>KRV’s two - day summit have to say</p></div>
    <div class="blog-button">Visit our blog <svg width="11" height="12" viewBox="0 0 11 12"><path d="M0 0L11 6L0 12Z" fill="#fff"/></svg></div>
  </section>

  <div class="slider-dots"><span class="is-active"></span><span></span><span></span><span></span><span></span></div>

  <nav class="main-nav">
    <a>Company</a><a>Products &amp; Service</a><a>Learning Center</a><a>Events</a><a>KRV News</a><a>Contact Us</a>
  </nav>
  <svg class="nav-curve" viewBox="0 0 720 16" preserveAspectRatio="none" aria-hidden="true">
    <path d="M0 14Q360 -6 720 14" fill="none" stroke="#c9c9c9" stroke-width="3"/>
  </svg>

  <div class="feature-divider" style="left:252px"></div>
  <div class="feature-divider" style="left:461px"></div>

  <article class="feature" style="left:44px">
    <svg class="feature-icon" viewBox="0 0 68 74" role="img" aria-label="Green badge with a light bulb pictogram">
      <path d="M34 2L65 19V55L34 72L3 55V19Z" fill="var(--green)"/>
    </svg>
    <h2>Innovation.</h2>
    <div class="feature-text"><span>Lorem ipsum dolor sit amet, consectetur adipiscing elit. Proin placerat nulla massa, a condimentum leo tincidunt vel.</span><span>Consectetur adipiscing elit.<br>Proin placerat nulla massa,<br>a condimentum leo.</span></div>
    <div class="feature-button">Learn More <svg width="11" height="12" viewBox="0 0 11 12"><path d="M0 0L11 6L0 12Z" fill="#fff"/></svg></div>
  </article>

  <article class="feature" style="left:254px">
    <svg class="feature-icon" viewBox="0 0 68 74" role="img" aria-label="Orange badge with a workflow pictogram">
      <path d="M34 2L65 19V55L34 72L3 55V19Z" fill="var(--amber)"/>
    </svg>
    <h2>Automation.</h2>
    <div class="feature-text"><span>Lorem ipsum dolor sit amet, consectetur adipiscing elit. Aenean facilisis interdum. Vivamus et sapien varius.</span><span>Dolor sit amet, consectetur adipiscing elit. Aenean facilisis interdum.</span></div>
    <div class="feature-button">Order Now <svg width="11" height="12" viewBox="0 0 11 12"><path d="M0 0L11 6L0 12Z" fill="#fff"/></svg></div>
  </article>

  <article class="feature" style="left:464px">
    <svg class="feature-icon" viewBox="0 0 68 74" role="img" aria-label="Blue badge with a laboratory flask pictogram">
      <path d="M34 2L65 19V55L34 72L3 55V19Z" fill="var(--azure)"/>
    </svg>
    <h2>Research.</h2>
    <div class="feature-text"><span>Lorem ipsum dolor sit amet, consectetur adipiscing elit. Class aptent taciti sociosqu ad litora torquent per conubia.</span><span>Amet, consectetur adipiscing elit.<br>Class aptent taciti sociosqu ad litora torquent per.</span></div>
    <div class="feature-button">The Challenge <svg width="11" height="12" viewBox="0 0 11 12"><path d="M0 0L11 6L0 12Z" fill="#fff"/></svg></div>
  </article>

  <footer class="site-footer">
    Home<span class="sep">|</span>Company<span class="sep">|</span>Products &amp; Services<span class="sep">|</span>Contact Us<span class="sep">|</span>Site Map<span class="sep">|</span>Privacy Policy
  </footer>
  <div class="copyright">Terms © 2013 Demo Site.</div>
</main>
</body>
</html>
```